Im starting a new speed dating business, called 'marigold speed dating', in my local area. I'm looking

I live in a semi-rural, quite alternative & progressive, spiritual community (Byron Bay, Australia). I want to launch the first event in 4 weeks! I would like a design for a flyer that catches people's attention, not in a 'screaming' way, but beautiful, interesting, inviting......They'll be monthly events, possibly with different themes; silent, tantric, spiritual.....etc.
I like to create a 'brand', where design for flyer, website, Fb, logo is aligned and easily recognizable.
The singles events are to be safe, sacred, playful, deep, fun & well facilitated.
It's for people serious about meeting & connecting authentically with others, with an interest to partner. Thank you
Target Market(s)
Single men & women, intelligent, conscious, middle class, 25-55yrs
Industry/Entity Type
Dating
Look and feel

```html
<!DOCTYPE html>
<html lang="en">
<head>
<meta charset="utf-8">
<title>Marigold Speed Dating</title>
<link href="https://fonts.googleapis.com/css2?family=Arimo:ital,wght@0,400;0,700;1,400&family=Kaushan+Script&family=Raleway:wght@300&display=swap" rel="stylesheet">
<style>
  :root{
    --orange:#e9742a;
    --orange-band:#ec8a2c;
    --grey-title:#6f6f6f;
    --ink:#2c2a33;
    --teal:#1fa7a0;
    --lavender:#b8a3c9;
    --lilac-soft:#ece4f0;
    --paper:#ffffff;
    --canopy:#7d8a5e;
    --sand:#d8cfc0;
  }
  html,body{margin:0;padding:0;overflow:hidden;background:var(--paper);}
  .flyer{position:relative;width:853px;height:1200px;overflow:hidden;background:var(--paper);font-family:"Arimo",Arial,sans-serif;color:var(--ink);}
  .hero-photo{position:absolute;left:0;top:0;width:853px;height:1012px;}
  .title{position:absolute;left:190px;top:200px;width:500px;margin:0;font-weight:normal;text-align:center;}
  .title-script{font-family:"Kaushan Script",cursive;color:var(--orange);font-size:96px;line-height:1.05;display:block;}
  .title-caps{font-family:"Raleway",sans-serif;font-weight:300;color:var(--grey-title);font-size:54px;letter-spacing:5px;display:block;white-space:nowrap;margin-top:2px;}
  .intro{position:absolute;left:352px;top:462px;width:462px;font-size:14px;line-height:1.2;color:var(--ink);}
  .intro p{margin:0 0 16px;}
  .tagline{position:absolute;left:40px;top:788px;width:773px;text-align:center;font-family:"Kaushan Script",cursive;color:var(--teal);font-size:31px;white-space:nowrap;}
  .booking{position:absolute;left:42px;top:845px;width:770px;font-size:14.5px;line-height:1.25;font-weight:700;}
  .booking p{margin:0;}
  .call{position:absolute;left:42px;top:908px;font-weight:700;font-size:27px;line-height:1.3;color:var(--ink);}
  .band{position:absolute;left:0;top:1012px;width:853px;height:188px;background:var(--orange-band);}
  .band-text{position:absolute;left:42px;top:1035px;width:600px;margin:0;font-style:italic;color:var(--paper);font-size:15px;line-height:1.3;}
  .portrait{position:absolute;left:672px;top:990px;width:150px;height:190px;}
</style>
</head>
<body>
<div class="flyer">
  <svg class="hero-photo" role="img" aria-label="Photo of a couple walking hand in hand along a beach beneath spreading tree branches, fading to soft lavender and white" viewBox="0 0 853 1012">
    <defs>
      <linearGradient id="sky" x1="0" y1="0" x2="0" y2="1">
        <stop offset="0" stop-color="var(--canopy)"/>
        <stop offset="0.35" stop-color="#b9bea0"/>
        <stop offset="0.7" stop-color="var(--sand)"/>
        <stop offset="1" stop-color="var(--lavender)"/>
      </linearGradient>
      <radialGradient id="fadeRight" cx="0.85" cy="0.62" r="0.65">
        <stop offset="0" stop-color="#fff" stop-opacity="0.95"/>
        <stop offset="0.55" stop-color="#fff" stop-opacity="0.7"/>
        <stop offset="1" stop-color="#fff" stop-opacity="0"/>
      </radialGradient>
      <linearGradient id="fadeDown" x1="0" y1="0" x2="0" y2="1">
        <stop offset="0.5" stop-color="#fff" stop-opacity="0"/>
        <stop offset="0.78" stop-color="var(--lilac-soft)" stop-opacity="0.85"/>
        <stop offset="1" stop-color="#fff" stop-opacity="1"/>
      </linearGradient>
    </defs>
    <rect width="853" height="1012" fill="url(#sky)"/>
    <rect width="853" height="1012" fill="url(#fadeRight)"/>
    <rect width="853" height="1012" fill="url(#fadeDown)"/>
  </svg>

  <h1 class="title">
    <span class="title-script">Marigold</span>
    <span class="title-caps">SPEED DATING</span>
  </h1>

  <div class="intro">
    <p>This massive issue, you can read our five-star review of Orbitfall (in cinemas October 3), wherein we wonder if it's the year's best movie. In this massive issue, you can read our five-star review of Orbitfall (in cinemas October 3), wherein we wonder if it's the year's best movie.</p>
    <p>This massive issue, you can read our five-star review of Orbitfall (in cinemas October 3), wherein we wonder if it's the year's best movie. In this massive issue, you can read our five-star review of Orbitfall (in cinemas October 3), wherein we wonder if it's the year's best movie.</p>
    <p>This massive issue, you can read our five-star review of Orbitfall (in cinemas October 3), wherein we wonder if it's the year's best movie. In this massive issue, you can read our five-star review of Orbitfall (in cinemas October 3), wherein we wonder if it's the year's best movie.</p>
  </div>

  <div class="tagline">safe, sacred, playful, deep, fun &amp; well facilitated</div>

  <div class="booking">
    <p>BOOKING DETAILS: you can read our five-star review of Orbitfall (in cinemas October 3), wherein we wonder if it's the year's best movie. In this massive issue, you can read our five-star review of Orbitfall (in cinemas October 3), wherein we wonder if it's the year's best movie.</p>
  </div>

  <div class="call">BOOK EARLY TO GET A PLACING CALL<br>1800 555 0142 ETC...</div>

  <div class="band"></div>
  <p class="band-text">In this massive issue, you can read our five-star review of Orbitfall (in cinemas October 3), wherein we wonder if it's the year's best movie. (It's certainly the most stressful.) You can also listen to our chats with Tomas Wendell, star of Redline, and Elliot Marsh, and The Quiet Harbour should give you a fair idea. So, scroll down and enjoy!</p>

  <svg class="portrait" role="img" aria-label="Portrait photo of the event host" viewBox="0 0 150 190">
    <defs>
      <linearGradient id="portraitTone" x1="0" y1="0" x2="0" y2="1">
        <stop offset="0" stop-color="#cfc7bd"/>
        <stop offset="1" stop-color="#5b5f66"/>
      </linearGradient>
    </defs>
    <rect width="150" height="190" fill="url(#portraitTone)"/>
  </svg>
</div>
</body>
</html>
```